Cargo Van Car Wrap

We have purchased a new car and are looking for a design.

2023 Torvane 3400 Cargo Van 170"

Target Market(s)

Home Improvement - Kitchen and Bath Remodeling , Home Additions, Sunroom, Deck, Patio, Porch

Industry/Entity Type

Interior Remodeling , Home Additions . Kitchen and Bath Remodeling

Font styles to use
Sans Serif

Colors

Designer to choose colors to be used in the design.

Requirements
Must have
• Kitchen and Bathroom Pictures
Nice to have
• Office address , website, phone number and promition. 4817 Brindle Ave Silver Spring MD 20847 , www.zentrokitchenandbath.com - 3015550187

```html
<!DOCTYPE html>
<html lang="en">
<head>
<meta charset="utf-8">
<title>Zentro Kitchen &amp; Bath – Cargo Van Wrap</title>
<link rel="stylesheet" href="https://fonts.googleapis.com/css2?family=Montserrat:wght@500;600;700;800&display=swap">
<style>
  :root{
    --bg:#ffffff;
    --body:#f4f4f6;
    --body-edge:#d9dade;
    --rocker:#4b4c52;
    --glass:#2c2f36;
    --purple:#8e1a9c;
    --purple-soft:#b35bc0;
    --ink:#111114;
    --grey-text:#55565c;
    --white:#ffffff;
  }
  *{margin:0;padding:0;box-sizing:border-box}
  html,body{width:1200px;height:675px;overflow:hidden;background:var(--bg)}
  .canvas{position:relative;width:1200px;height:675px;font-family:"Montserrat",sans-serif}
  .van-art{position:absolute;left:0;top:0}
  .brand{position:absolute;left:815px;top:158px;width:270px;text-align:center;color:var(--grey-text)}
  .brand-name{font-size:54px;font-weight:600;letter-spacing:4px;line-height:1;color:var(--ink)}
  .brand-sub{font-size:17px;font-weight:500;letter-spacing:2px;margin-top:10px;color:var(--grey-text)}
  .brand-services{font-size:10.5px;font-weight:700;line-height:1.45;margin-top:20px;color:var(--grey-text)}
  .address{position:absolute;left:210px;top:336px;width:150px;text-align:center;font-size:13.5px;font-weight:700;line-height:1.3;color:var(--ink)}
  .cta{position:absolute;left:420px;top:343px;font-size:36px;font-weight:800;letter-spacing:1.5px;color:var(--ink);line-height:42px}
  .phone{position:absolute;left:770px;top:343px;font-size:36px;font-weight:700;letter-spacing:1.5px;color:var(--white);line-height:42px}
  .website{position:absolute;left:320px;top:428px;font-size:19px;font-weight:700;letter-spacing:.5px;color:var(--ink)}
</style>
</head>
<body>
<div class="canvas">
  <svg class="van-art" width="1200" height="675" viewBox="0 0 1200 675">
    <defs>
      <linearGradient id="kitchen-tones" x1="0" y1="0" x2="1" y2="1">
        <stop offset="0" stop-color="#e9e7e3"/>
        <stop offset="0.6" stop-color="#c9c3ba"/>
        <stop offset="1" stop-color="#8a7f72"/>
      </linearGradient>
      <linearGradient id="interior-tones" x1="0" y1="0" x2="1" y2="1">
        <stop offset="0" stop-color="#d8d6d2"/>
        <stop offset="1" stop-color="#6f5a48"/>
      </linearGradient>
      <linearGradient id="bath-tones" x1="0" y1="0" x2="1" y2="1">
        <stop offset="0" stop-color="#eeeeec"/>
        <stop offset="1" stop-color="#b9a58a"/>
      </linearGradient>
    </defs>

    <!-- van body side -->
    <path class="van-body" d="M40,470 L40,370 Q48,330 120,310 L250,170 Q275,118 330,114 L1095,100 Q1140,100 1148,150 L1155,470 Q1155,505 1125,505 L80,505 Q40,505 40,470 Z" fill="var(--body)" stroke="var(--body-edge)" stroke-width="2"/>
    <path class="rocker-band" d="M42,440 L1155,440 L1155,470 Q1155,505 1125,505 L80,505 Q42,505 42,470 Z" fill="var(--rocker)"/>
    <path class="side-window" d="M225,190 L255,160 Q265,150 300,150 L362,150 L362,285 L205,290 Z" fill="var(--glass)"/>

    <!-- photo collage -->
    <polygon role="img" aria-label="Photo of a modern white kitchen with range hood and island" points="470,105 800,100 770,285 430,290" fill="url(#kitchen-tones)"/>
    <polygon role="img" aria-label="Photo of a bright open-plan kitchen with pendant light and windows" points="800,100 1100,98 1108,150 800,150" fill="url(#interior-tones)"/>
    <polygon role="img" aria-label="Photo of a kitchen island with blue bar stools" points="430,260 555,258 535,332 420,334" fill="url(#kitchen-tones)"/>
    <polygon role="img" aria-label="Photo of a wooden spiral staircase" points="565,258 665,258 645,332 545,332" fill="url(#interior-tones)"/>
    <polygon role="img" aria-label="Photo of a remodeled bathroom vanity with round mirror" points="675,258 790,258 770,332 655,332" fill="url(#bath-tones)"/>
    <polygon role="img" aria-label="Photo of a finished room with light wood flooring" points="790,300 1110,300 1110,335 780,335" fill="url(#bath-tones)"/>

    <!-- accent frames -->
    <polyline points="470,105 430,290" stroke="var(--purple)" stroke-width="3" fill="none"/>
    <polyline points="555,258 535,332" stroke="var(--purple)" stroke-width="3" fill="none"/>
    <polygon points="450,105 520,105 495,170" fill="var(--ink)"/>

    <!-- brand panel -->
    <polygon class="brand-panel" points="830,145 1108,145 1110,305 790,305" fill="var(--white)" opacity="0.95"/>

    <!-- bands -->
    <polygon class="cta-band" points="395,340 770,340 755,388 380,388" fill="var(--purple)"/>
    <polygon class="phone-band" points="770,340 1110,340 1110,388 755,388" fill="var(--ink)"/>

    <!-- small accents -->
    <polygon points="355,140 370,150 355,160" fill="var(--purple)"/>
    <polygon points="590,455 600,440 610,455" fill="var(--purple)"/>
    <polygon points="100,390 115,380 112,396" fill="var(--purple-soft)"/>
    <g fill="none" stroke="var(--purple-soft)" stroke-width="1.2">
      <circle cx="700" cy="450" r="8"/><circle cx="700" cy="450" r="15"/><circle cx="700" cy="450" r="22"/><circle cx="700" cy="450" r="29"/>
      <circle cx="70" cy="400" r="8"/><circle cx="70" cy="400" r="15"/><circle cx="70" cy="400" r="22"/>
    </g>
  </svg>

  <div class="brand">
    <div class="brand-name">ZENTRO</div>
    <div class="brand-sub">KITCHEN &amp; BATH</div>
    <div class="brand-services">Experts In Bath &amp; Kitchen Remodelling,<br>Interior House Painting, Flooring,<br>Cabinet &amp; Counter-tops and Tiles &amp; Ceramic</div>
  </div>

  <div class="address">4817 BRINDLE AVE<br>SILVER SPRING<br>MD 20847</div>
  <div class="cta">CALL TO BOOK</div>
  <div class="phone">(301) 555-0187</div>
  <div class="website">www.zentrokitchenandbath.com</div>
</div>
</body>
</html>
```